Design a label for a dog shampoo names plovik, the sell point of this series of shampoo is “just like wash your dogs with milk, not harm for your hand ”, the style could be gentle or professional or even amazing.

Use only 2 colors in the design job, the color of our logo could be changed, it depends on your whole page. Please design in CDR or ai.

update:
Pls do more change with the fonts when you design the front page, including title and details. Try more styles of fonts. Addition, this design will be printed on the bottle, no a label stick on it.
Updates

Do not put a real dog or animal on the page, Pay more attention to the types of fonts

Reason: Expect for more design idea.

Target Market(s)

people 20-30 years old who have dogs and cats at home

Industry/Entity Type

It Professional

Requirements
Nice to have
• It would be nice if you add some detail words in the design of the right side.

```html
<!DOCTYPE html>
<html lang="en">
<head>
<meta charset="utf-8">
<title>plovik Milk Shampoo – Bottle Print</title>
<link href="https://fonts.googleapis.com/css2?family=Oswald:wght@400;500&family=Arvo:wght@700&family=Roboto+Condensed:wght@400;700&display=swap" rel="stylesheet">
<style>
  :root {
    --teal: #1aa5c3;
    --grey: #8c8c8c;
    --grey-dark: #5f5f5f;
    --print-base: #ffffff;
    --backdrop: #d6d6d6;
    --ornament-tone: #ececec;
  }
  * { margin: 0; padding: 0; box-sizing: border-box; }
  html, body { width: 1200px; height: 1200px; overflow: hidden; }
  body {
    background: var(--backdrop);
    font-family: "Roboto Condensed", "Arial Narrow", sans-serif;
    color: var(--grey-dark);
    position: relative;
  }
  .print-area {
    position: absolute;
    top: 430px;
    width: 380px;
    height: 580px;
    background: var(--print-base);
    border-radius: 14px;
  }
  .print-front { left: 205px; }
  .print-back { left: 607px; }

  /* Front */
  .brand-name {
    position: absolute;
    left: 0; right: 0;
    text-align: center;
    font-family: "Roboto Condensed", sans-serif;
    font-weight: 700;
    color: var(--teal);
    line-height: 1;
  }
  .print-front .brand-name { top: 55px; font-size: 54px; }
  .ornament-frame {
    position: absolute;
    left: 50px; top: 130px;
    width: 280px; height: 430px;
    border-radius: 60px;
    background: radial-gradient(ellipse at center, var(--print-base) 55%, var(--ornament-tone) 100%);
  }
  .front-copy {
    position: absolute;
    left: 0; right: 0;
    text-align: center;
  }
  .front-subtitle {
    top: 172px;
    font-family: "Oswald", sans-serif;
    font-weight: 500;
    font-size: 16px;
    line-height: 20px;
    color: var(--grey);
  }
  .front-title {
    top: 215px;
    font-family: "Oswald", sans-serif;
    font-weight: 500;
    font-size: 30px;
    letter-spacing: 1px;
    color: var(--grey);
  }
  .front-milk {
    top: 262px;
    font-family: "Arvo", serif;
    font-weight: 700;
    font-size: 52px;
    letter-spacing: 2px;
    color: var(--teal);
  }
  .front-benefits {
    top: 345px;
    font-family: "Oswald", sans-serif;
    font-weight: 500;
    font-size: 16px;
    line-height: 20px;
    color: var(--grey);
  }
  .volume-tag {
    position: absolute;
    left: 148px; top: 412px;
    width: 84px; height: 26px;
    background: var(--teal);
    border-radius: 4px;
    color: var(--print-base);
    font-family: "Oswald", sans-serif;
    font-size: 16px;
    line-height: 26px;
    text-align: center;
  }

  /* Back */
  .print-back .brand-name { top: 40px; font-size: 30px; }
  .back-content {
    position: absolute;
    left: 70px; right: 62px; top: 96px;
    font-size: 8.6px;
    line-height: 10.4px;
  }
  .back-title {
    font-family: "Oswald", sans-serif;
    font-weight: 500;
    font-size: 14px;
    color: var(--grey-dark);
    margin-bottom: 4px;
  }
  .directions-box {
    position: relative;
    margin-top: 22px;
    border: 1px solid var(--grey);
    border-radius: 5px;
    padding: 12px 8px 6px;
  }
  .directions-label {
    position: absolute;
    top: -8px; left: 50%;
    transform: translateX(-50%);
    background: var(--grey-dark);
    color: var(--print-base);
    font-weight: 700;
    font-size: 10px;
    line-height: 15px;
    padding: 0 8px;
    border-radius: 4px;
  }
  .directions-list { list-style: none; }
  .section-heading {
    margin-top: 16px;
    text-align: center;
    font-weight: 700;
    font-size: 9.5px;
    text-decoration: underline;
  }
  .ingredients {
    text-align: center;
    font-size: 10px;
    margin-top: 6px;
  }
  .section-text { margin-top: 8px; }
</style>
</head>
<body>
  <section class="print-area print-front">
    <div class="brand-name">plovik</div>
    <div class="ornament-frame" role="img" aria-label="Decorative grey swirl border framing the product name"></div>
    <div class="front-copy front-subtitle">SUPER-CONDITIONING<br>AND NUTRIENT</div>
    <div class="front-copy front-title">SHAMPOO</div>
    <div class="front-copy front-milk">MILK</div>
    <div class="front-copy front-benefits">MOISTURE-RICH<br>SMOOTH AND SILKY</div>
    <div class="volume-tag">1000 ml</div>
  </section>

  <section class="print-area print-back">
    <div class="brand-name">plovik</div>
    <div class="back-content">
      <h2 class="back-title">Super-Conditioning &amp; Nutrient Shampoo</h2>
      <p>is a specially formulated shampoo, rich in conditioners picked up from milk which subdivide and balance nutrition of pet's coat. More easier and better assimilate for coat from base to the end after using. With the help of minus-ion, the balancer of nutrition, rinses out quickly and completely to leave a soft, sparkling, and smooth coat. Safe and gentle enough to be used every day. Safe for even the most sensitive skin and coat, puppies, lactating bitches and cats.</p>

      <div class="directions-box">
        <span class="directions-label">DIRECTIONS</span>
        <ul class="directions-list">
          <li>a) Before shampooing, brush out pet's coat.</li>
          <li>b) Saturate dog's coat with lukewarm water.</li>
          <li>c) Dispense a small amount of shampoo into the palm of your hand.</li>
          <li>d) To clean coat, start at dog's head and work back towards the tail.</li>
          <li>e) Avoid getting shampoo into the dog's eyes and ears.</li>
          <li>f) Rinse coat several times with lukewarm water.</li>
          <li>g) Towel dry and gently comb or brush coat.</li>
        </ul>
      </div>

      <h3 class="section-heading">ACTIVE INGREDIENTS:</h3>
      <p class="ingredients">Hypochlorous Acid, Sodium Hypochlorite</p>

      <h3 class="section-heading">USE PRECAUTIONS:</h3>
      <p class="section-text">Harmful if swallowed. Do not inhale. Discontinue use if irritation develops and contact your veterinarian. For animal use only. Not for human use. Keep out of reach of children. Do not decant into smaller containers. Not for injection. Always consult with a Veterinarian for systemic conditions.</p>

      <h3 class="section-heading">STORAGE AND DISPOSAL</h3>
      <p class="section-text">Keep out of the touch of children. Replace Cap. Wrap in several layers of newspaper and discard in trash.</p>
    </div>
  </section>
</body>
</html>
```